Business Card for a Floral & Decorating Business

I would like to take my current logo and create a better business card. I am looking for elegance as I am a florist and event decorator. My logo has multiple colour options. I like colours like green, purple, pink and orange, I think I would like a white card, open to black back ground. I want it to feel elegant and romantic. I like metallic lettering that maybe is indented in the paper, I also like glossy paper. I have a full logo already as well as a badge. I have attached both in multiple colours.m

Target Market(s)

Weddings, special events, floral customers

Industry/Entity Type

Floral and decorating

Contact Information for Business Card

Phone number, email, instagram, facebook, title, name, logo

Font styles to use
Script

Requirements
Nice to have
• Elegant

```html
<!DOCTYPE html>
<html lang="en">
<head>
<meta charset="utf-8">
<title>Marlowe Fenn — Business Card</title>
<link href="https://fonts.googleapis.com/css2?family=Libre+Baskerville:wght@400;700&family=Montserrat:wght@400&display=swap" rel="stylesheet">
<style>
  :root {
    --backdrop: #999999;
    --card: #ffffff;
    --sage: #5e877c;
    --sage-tint: #e3ece9;
    --ink: #1f2326;
  }
  * { margin: 0; padding: 0; box-sizing: border-box; }
  html, body { width: 1200px; height: 1059px; overflow: hidden; }
  body { background: var(--backdrop); position: relative; font-family: "Montserrat", sans-serif; color: var(--ink); }

  .card {
    position: absolute;
    width: 690px;
    height: 392px;
    background: var(--card);
    border-radius: 16px;
    overflow: hidden;
  }
  .card--front { left: 256px; top: 89px; }
  .card--back { left: 254px; top: 569px; }

  .brand-name {
    font-family: "Libre Baskerville", serif;
    font-weight: 400;
    color: var(--sage);
    white-space: nowrap;
  }
  .card--front .brand-name {
    position: absolute;
    left: 32px;
    top: 62px;
    font-size: 30px;
    letter-spacing: 1px;
  }

  .name-bar {
    position: absolute;
    left: 0;
    top: 157px;
    width: 18px;
    height: 40px;
    background: var(--sage);
  }
  .person-name {
    position: absolute;
    left: 32px;
    top: 153px;
    font-family: "Libre Baskerville", serif;
    font-weight: 700;
    font-size: 25px;
    color: var(--sage);
    letter-spacing: 0.3px;
  }
  .person-title {
    position: absolute;
    left: 32px;
    top: 183px;
    font-size: 16px;
  }
  .address {
    position: absolute;
    left: 32px;
    top: 223px;
    font-size: 16px;
    line-height: 21px;
  }
  .contact-list {
    position: absolute;
    left: 32px;
    top: 281px;
    list-style: none;
    font-size: 16px;
  }
  .contact-list li {
    display: flex;
    align-items: center;
    gap: 6px;
    height: 27px;
  }
  .contact-list svg { width: 12px; height: 12px; fill: var(--sage); flex: none; }

  .floral-area {
    position: absolute;
    left: 420px;
    top: 26px;
    width: 242px;
    height: 341px;
    background: linear-gradient(160deg, var(--sage-tint), #cfdfda);
    border-radius: 4px;
  }

  .back-mark {
    position: absolute;
    left: 50%;
    top: 88px;
    width: 64px;
    height: 64px;
    margin-left: -32px;
    border-radius: 50%;
    background: var(--sage);
  }
  .card--back .brand-name {
    position: absolute;
    left: 0;
    right: 0;
    top: 196px;
    text-align: center;
    font-size: 46px;
    letter-spacing: 2px;
  }
</style>
</head>
<body>

<section class="card card--front" aria-label="Business card front">
  <div class="brand-name">Marlowe Fenn</div>

  <div class="name-bar"></div>
  <h1 class="person-name">ELENA HART</h1>
  <p class="person-title">CEO/Founder</p>

  <p class="address">48 Willow Row Suite B<br>Fairview CA, 95012</p>

  <ul class="contact-list">
    <li>
      <svg viewBox="0 0 24 24" aria-hidden="true"><path d="M6.6 10.8a15 15 0 0 0 6.6 6.6l2.2-2.2c.3-.3.7-.4 1-.2 1.1.4 2.3.6 3.6.6.6 0 1 .4 1 1V20c0 .6-.4 1-1 1A17 17 0 0 1 3 4c0-.6.4-1 1-1h3.5c.6 0 1 .4 1 1 0 1.3.2 2.5.6 3.6.1.3 0 .7-.2 1z"/></svg>
      (123) 456-7890
    </li>
    <li>
      <svg viewBox="0 0 24 24" aria-hidden="true"><path d="M2 5h20v14H2z M2 5l10 8 10-8" /></svg>
      info@websitename.com
    </li>
    <li>
      <svg viewBox="0 0 24 24" aria-hidden="true"><path d="M12 2a10 10 0 1 0 0 20 10 10 0 0 0 0-20zm0 2c1 1.3 1.8 3.4 2 6h-4c.2-2.6 1-4.7 2-6zm-3.9 1A12 12 0 0 0 8 10H4.3A8 8 0 0 1 8.1 5zm7.8 0a8 8 0 0 1 3.8 5H16a12 12 0 0 0-.1-5zM4.3 12H8c.1 2 .5 3.7 1.1 5A8 8 0 0 1 4.3 12zm5.7 0h4c-.2 2.6-1 4.7-2 6-1-1.3-1.8-3.4-2-6zm6 0h3.7a8 8 0 0 1-4.8 5c.6-1.3 1-3 1.1-5z"/></svg>
      www.websitename.com
    </li>
  </ul>

  <div class="floral-area" role="img" aria-label="Line-drawn floral arrangement with leaves and open blooms in sage green"></div>
</section>

<section class="card card--back" aria-label="Business card back">
  <div class="back-mark"></div>
  <div class="brand-name">Marlowe Fenn</div>
</section>

</body>
</html>
```